Ashcombe Ridge Business Cards

We need business card designs for a modern home development, Ashcombe Ridge. We would like to see modern looking designs- clean and simple but striking. I've attached some images of one of the homes so you can see the style of the homes we are putting on the market and perhaps they will inspire your design! I've also attached the logo- both horizontal and vertical. We need to use the logo on the card. I've also attached a sign that has a map of the development. If you can use that and still keep the card nice and clean, great. If not, it's not a problem to leave the map out completely.

```html
<!DOCTYPE html>
<html lang="en">
<head>
<meta charset="utf-8">
<title>Ashcombe Ridge Business Cards</title>
<link href="https://fonts.googleapis.com/css2?family=Open+Sans:wght@400;600;700&display=swap" rel="stylesheet">
<style>
  :root {
    --bg-light: #c9d3da;
    --bg-dark: #8b9aa6;
    --card-clear: rgba(236, 242, 246, 0.78);
    --card-edge: rgba(255, 255, 255, 0.85);
    --band: #0b1a20;
    --teal: #1a8aa3;
    --ink: #0d1f27;
    --text-light: #e8eef1;
    --ghost: rgba(20, 40, 50, 0.22);
    --map-line: #1f8fa8;
  }
  * { margin: 0; padding: 0; box-sizing: border-box; }
  html, body { width: 1200px; height: 792px; overflow: hidden; }
  body {
    background: radial-gradient(ellipse at 50% 35%, var(--bg-light) 0%, var(--bg-dark) 100%);
    font-family: "Open Sans", Arial, sans-serif;
    position: relative;
  }
  .card {
    position: absolute;
    top: 230px;
    width: 522px;
    height: 337px;
    border-radius: 18px;
    overflow: hidden;
    background: var(--card-clear);
    box-shadow: 0 0 0 1px var(--card-edge) inset, 0 8px 22px rgba(0, 0, 0, 0.18);
  }
  .card--front { left: 55px; }
  .card--back { left: 626px; }
  .card__stripe {
    position: absolute; left: 0; right: 0; top: 163px; height: 11px;
    background: var(--teal);
  }
  .card__band {
    position: absolute; left: 0; right: 0; top: 174px; bottom: 0;
    background: var(--band);
  }
  .wordmark {
    position: absolute; left: 84px; top: 62px;
    display: flex; align-items: center; gap: 14px;
  }
  .wordmark__square {
    width: 52px; height: 52px; background: var(--teal);
  }
  .wordmark__name {
    font-weight: 700; font-size: 40px; letter-spacing: 0.5px;
    color: var(--ink); line-height: 1;
  }
  .wordmark--ghost { left: 88px; }
  .wordmark--ghost .wordmark__square { background: var(--ghost); }
  .wordmark--ghost .wordmark__name { color: var(--ghost); }
  .holder {
    position: absolute; left: 25px; top: 180px;
  }
  .holder__name {
    font-weight: 600; font-size: 17px; color: var(--teal); line-height: 1.2;
  }
  .holder__title {
    font-weight: 700; font-size: 11px; color: var(--text-light); margin-top: 2px;
  }
  .contacts {
    position: absolute; left: 25px; top: 238px; list-style: none;
  }
  .contacts li {
    display: flex; align-items: center; gap: 6px;
    font-size: 13px; color: var(--text-light); height: 18.5px;
  }
  .contacts svg { width: 12px; height: 12px; fill: var(--teal); flex: none; }
  .map {
    position: absolute; left: 144px; top: 177px; width: 237px; height: 148px;
    background: linear-gradient(135deg, #0f2a33 0%, #123640 50%, #0f2a33 100%);
    border: 1px solid var(--map-line);
  }
</style>
</head>
<body>
  <section class="card card--front">
    <div class="wordmark">
      <span class="wordmark__square"></span>
      <span class="wordmark__name">ASHCOMBE RIDGE</span>
    </div>
    <div class="card__stripe"></div>
    <div class="card__band"></div>
    <div class="holder">
      <p class="holder__name">Daniel K. Harlow</p>
      <p class="holder__title">Developer, Investor</p>
    </div>
    <ul class="contacts">
      <li>
        <svg viewBox="0 0 24 24" aria-hidden="true"><path d="M6.6 10.8a15.1 15.1 0 0 0 6.6 6.6l2.2-2.2a1 1 0 0 1 1-.25 11.4 11.4 0 0 0 3.6.57 1 1 0 0 1 1 1V20a1 1 0 0 1-1 1A17 17 0 0 1 3 4a1 1 0 0 1 1-1h3.5a1 1 0 0 1 1 1c0 1.25.2 2.45.57 3.6a1 1 0 0 1-.25 1z"/></svg>
        555.318.4402
      </li>
      <li>
        <svg viewBox="0 0 24 24" aria-hidden="true"><path d="M7 1h10a2 2 0 0 1 2 2v18a2 2 0 0 1-2 2H7a2 2 0 0 1-2-2V3a2 2 0 0 1 2-2zm0 3v14h10V4zm5 15.5a1 1 0 1 0 0 2 1 1 0 0 0 0-2z"/></svg>
        555.260.7719
      </li>
      <li>
        <svg viewBox="0 0 24 24" aria-hidden="true"><path d="M2 6l10 7 10-7v12a2 2 0 0 1-2 2H4a2 2 0 0 1-2-2zm1-2h18l-9 6.3z"/></svg>
        danielkharlow@mailbridge.net
      </li>
      <li>
        <svg viewBox="0 0 24 24" aria-hidden="true"><path d="M12 2 1 12h3v9h6v-6h4v6h6v-9h3z"/></svg>
        2140 Fenwick Avenue, Portland, OR 97214
      </li>
    </ul>
  </section>

  <section class="card card--back">
    <div class="wordmark wordmark--ghost">
      <span class="wordmark__square"></span>
      <span class="wordmark__name">ASHCOMBE RIDGE</span>
    </div>
    <div class="card__stripe"></div>
    <div class="card__band"></div>
    <div class="map" role="img" aria-label="Line map of the development's streets and home lots"></div>
  </section>
</body>
</html>
```